Flyer Design Project

I provide workshops for teachers, students and parents on organization - specifically laying out 3 goals, their accompanying activities and actions in 3 three hour sessions.

Please go to my website to see my brain logo. I need a flyer with the information typed below. The information may be changed and/or added to in way you see fit to better communicate the organizational intent.This is not for speech therapy clients, rather, it is for any and everyone who needs help writing out goals.

I would like the design of the flyer to reflect the concept of organization in a unique way.

http://themindcraftstudyhouse.com/wp-content/uploads/2012/02/websitelogo2.jpg

ORGANIZATION

Write out your goals for the year.

How to organize your life in 3 easy steps.
Have fun organizing your life and plans.
Join a group of people dedicated to organizing all areas of life.
Complete your tasks in a fast, fun game format.
Walk away with your major goals broken down into their component parts and organize on a yearly calendar.
Three 3 hour days spent in making your life happier, less stressed and with realistic picture of what needs to be accomplished.
more effective in everything I do.
Being organized helps free our minds, enjoy relationships more, feel happier, and have greater meaning in life.

You will walk away with detailed plans for 2013.

COST: $600 for all three days.

WHO: Led by Maren Holtby, Cognitive Speech Therapist
WHERE: 4971 E Pruett Ave
Kennewick, WA 99336
509-218-3907

Requirements
Must have
• My logo from my website. A unique organized appearance.

```html
<!DOCTYPE html>
<html lang="en">
<head>
<meta charset="utf-8">
<title>How to Organize Your Life – Workshop Flyer</title>
<link rel="stylesheet" href="https://fonts.googleapis.com/css2?family=Luckiest+Guy&display=swap">
<style>
  :root {
    --backdrop: #ebebe8;
    --paper: #ffffff;
    --header-top: #fffbe6;
    --header-bottom: #f6efbf;
    --rule-red: #d9432f;
    --rule-blue: #3b63b5;
    --brand-navy: #2b3f8f;
    --brand-dot: #1f3566;
    --sky: #1ea4e3;
    --cherry: #d2232a;
    --plum: #5b3393;
    --tangerine: #f58220;
    --gear-yellow: #fbf3c8;
    --wash-blue: #e3ecf6;
  }
  * { margin: 0; padding: 0; box-sizing: border-box; }
  html, body {
    width: 1200px; height: 900px; overflow: hidden;
    background: var(--backdrop);
  }
  .flyer {
    position: absolute; left: 296px; top: 56px;
    width: 608px; height: 787px;
    background: var(--paper);
    overflow: hidden;
    font-family: "Luckiest Guy", "Comic Sans MS", cursive;
  }
  .flyer__header {
    position: absolute; left: 0; top: 0; width: 608px; height: 96px;
    background: linear-gradient(180deg, var(--header-top), var(--header-bottom));
  }
  .flyer__rule {
    position: absolute; left: 0; top: 96px; width: 608px; height: 6px;
    border-top: 3px solid var(--rule-red);
    border-bottom: 3px solid var(--rule-blue);
  }
  .brand {
    position: absolute; left: 150px; top: 28px;
    display: flex; align-items: center; gap: 14px;
  }
  .brand__dot {
    width: 44px; height: 44px; border-radius: 50%;
    background: var(--brand-dot);
  }
  .brand__name {
    color: var(--brand-navy);
    font-size: 24px; letter-spacing: 0.5px; line-height: 1;
  }
  .flyer__backdrop {
    position: absolute; left: 0; top: 102px; width: 608px; height: 685px;
    background:
      radial-gradient(circle at 85% 15%, var(--gear-yellow) 0 18%, transparent 40%),
      radial-gradient(circle at 20% 35%, var(--gear-yellow) 0 15%, transparent 38%),
      radial-gradient(circle at 80% 85%, var(--gear-yellow) 0 14%, transparent 36%),
      linear-gradient(160deg, var(--wash-blue), #f4f7fb 60%, var(--wash-blue));
  }
  .copy { position: absolute; inset: 0; }
  .line {
    position: absolute; display: block; white-space: nowrap;
    line-height: 1; text-align: justify; text-align-last: justify;
  }
  .line--sky { color: var(--sky); }
  .line--cherry { color: var(--cherry); }
  .line--plum { color: var(--plum); }
  .line--tangerine { color: var(--tangerine); }
  .accent--plum { color: var(--plum); }
  .accent--tangerine { color: var(--tangerine); }
</style>
</head>
<body>
  <main class="flyer">
    <div class="flyer__backdrop" role="img" aria-label="Soft field of pale yellow interlocking gears over a light blue wash"></div>

    <header class="flyer__header">
      <div class="brand">
        <span class="brand__dot"></span>
        <span class="brand__name">The Mindcraft Study House</span>
      </div>
    </header>
    <div class="flyer__rule"></div>

    <section class="copy">
      <span class="line line--sky" style="left:216px;top:236px;width:193px;font-size:44px;">How to</span>
      <span class="line line--sky" style="left:172px;top:285px;width:277px;font-size:40px;letter-spacing:4px;">Organize</span>
      <span class="line line--sky" style="left:134px;top:325px;width:348px;font-size:20px;">Your life in 3 easy steps.</span>
      <span class="line line--cherry" style="left:128px;top:349px;width:356px;font-size:62px;">Have fun</span>
      <span class="line line--plum" style="left:125px;top:408px;width:359px;font-size:17px;">Organizing your life and plans.</span>
      <span class="line line--tangerine" style="left:126px;top:430px;width:365px;font-size:25px;">Join a group of people</span>
      <span class="line line--plum" style="left:134px;top:457px;width:346px;font-size:14px;">Dedicated to organizing all areas of life.</span>
      <span class="line line--tangerine" style="left:146px;top:475px;width:378px;font-size:27px;">Complete your tasks <span style="font-size:22px;">in</span></span>
      <span class="line line--tangerine" style="left:156px;top:505px;width:332px;font-size:21px;">A fast, fun game format.</span>
      <span class="line line--plum" style="left:167px;top:525px;width:337px;font-size:15px;">Walk away with your major goals</span>
      <span class="line line--plum" style="left:177px;top:541px;width:323px;font-size:11px;">Broken down into their component parts</span>
      <span class="line line--plum" style="left:177px;top:552px;width:323px;font-size:13px;">and organize on a yearly calendar.</span>
      <span class="line line--plum" style="left:176px;top:569px;width:313px;font-size:12px;">three 3 hour days spent in <span style="font-size:16px;">making your</span></span>
      <span class="line line--tangerine" style="left:176px;top:587px;width:313px;font-size:18px;">Life happier, less stressed</span>
      <span class="line line--plum" style="left:176px;top:605px;width:313px;font-size:12px;">and with realistic picture of what</span>
      <span class="line line--plum" style="left:176px;top:617px;width:243px;font-size:12px;">needs to be accomplished.</span>
      <span class="line line--sky" style="left:176px;top:633px;width:238px;font-size:20px;">More effective in</span>
      <span class="line line--sky" style="left:176px;top:654px;width:233px;font-size:22px;">Everything I do.</span>
      <span class="line line--plum" style="left:178px;top:678px;width:204px;font-size:12px;">Being organized helps free</span>
      <span class="line line--plum" style="left:170px;top:690px;width:212px;font-size:12px;">our minds, enjoy relationships</span>
      <span class="line line--plum" style="left:162px;top:702px;width:215px;font-size:13px;">more, feel happier, and have</span>
      <span class="line line--sky" style="left:141px;top:716px;width:236px;font-size:17px;">Greater meaning in life.</span>
    </section>
  </main>
</body>
</html>
```